Business Card Design Project

We require a professional business card designed for our consulting organisation that has the same theme and colours as our logo except for the grey.

Colours on the front should predominately be white however some reference to our logo colours except for the grey.

The back of the card should be have background colour that aligns with our logo colour.

Layout, style and design is up to the designer. So send through your designs

Details are attached in the word document project brief.

Target Market(s)

Target market are large corporate organisations

Industry/Entity Type

Business

Requirements
Must have
• Content on the front must have:

Dale Fenwick
Managing Director

P: 0412 557 208
E: Dale@braviotraxgroup.com
W: www.braviotraxgroup.com

Content on the back must have the words:
Alliances
Placement
Training
Support

Design Colours
Must align to our logo

```html
<!DOCTYPE html>
<html lang="en">
<head>
<meta charset="utf-8">
<title>BravioTrax Group – Business Card</title>
<link rel="stylesheet" href="https://fonts.googleapis.com/css2?family=Open+Sans:wght@400;600;700&display=swap">
<style>
  :root {
    --blue: #1a73c4;
    --blue-deep: #1360a8;
    --blue-light: #2a9ad8;
    --ink: #3a3f46;
    --rule: #9aa3ad;
    --paper: #ffffff;
    --paper-tint: #e8f0f8;
    --stage: #e4e6e9;
  }
  * { box-sizing: border-box; margin: 0; padding: 0; }
  html, body {
    width: 1200px; height: 900px; overflow: hidden;
    background: var(--stage);
    font-family: "Open Sans", Arial, sans-serif;
  }
  .canvas {
    width: 1200px; height: 900px;
    display: flex; flex-direction: column; align-items: center; justify-content: center;
    gap: 40px;
  }
  .card {
    position: relative;
    width: 700px; height: 400px;
    overflow: hidden;
    box-shadow: 0 6px 18px rgba(0,0,0,.18);
  }

  /* Front */
  .card--front {
    background: linear-gradient(160deg, var(--paper) 40%, var(--paper-tint) 100%);
  }
  .brand {
    position: absolute; left: 60px; top: 108px;
    display: flex; align-items: center; gap: 14px;
  }
  .brand__square { width: 34px; height: 34px; background: var(--blue); }
  .brand__name {
    font-size: 30px; font-weight: 700; color: var(--blue);
    letter-spacing: .5px;
  }
  .divider {
    position: absolute; left: 0; right: 0; top: 178px;
    height: 1px; background: var(--rule);
  }
  .person {
    position: absolute; right: 110px; top: 116px; text-align: right;
  }
  .person__name { font-size: 27px; font-weight: 600; color: var(--blue); line-height: 1.1; }
  .person__role { font-size: 16px; font-weight: 600; color: var(--ink); margin-top: 14px; }
  .contacts {
    position: absolute; left: 60px; top: 240px;
    list-style: none;
  }
  .contacts li {
    display: flex; align-items: center; gap: 14px;
    font-size: 16px; color: var(--ink); line-height: 1; margin-bottom: 16px;
  }
  .contacts svg { width: 16px; height: 16px; fill: var(--blue); flex: none; }
  .front-band {
    position: absolute; right: 0; top: 0; width: 700px; height: 400px;
  }

  /* Back */
  .card--back {
    background: linear-gradient(135deg, var(--blue-deep) 0%, var(--blue) 50%, var(--blue-light) 100%);
  }
  .services {
    position: absolute; left: 70px; top: 70px;
    list-style: none;
  }
  .services li {
    font-size: 36px; font-weight: 600; color: var(--paper);
    line-height: 1; margin-bottom: 34px;
  }
</style>
</head>
<body>
<main class="canvas">

  <section class="card card--front" aria-label="Business card front">
    <svg class="front-band" viewBox="0 0 700 400" aria-hidden="true">
      <polygon points="660,178 700,178 700,400 660,400" fill="#1a73c4"/>
    </svg>
    <div class="brand">
      <span class="brand__square"></span>
      <span class="brand__name">BravioTrax Group</span>
    </div>
    <div class="person">
      <p class="person__name">Dale Fenwick</p>
      <p class="person__role">Managing Director</p>
    </div>
    <div class="divider"></div>
    <ul class="contacts">
      <li>
        <svg viewBox="0 0 24 24"><path d="M6.6 10.8a15.1 15.1 0 0 0 6.6 6.6l2.2-2.2c.3-.3.7-.4 1-.2 1.1.4 2.3.6 3.6.6.6 0 1 .4 1 1V20c0 .6-.4 1-1 1A17 17 0 0 1 3 4c0-.6.4-1 1-1h3.5c.6 0 1 .4 1 1 0 1.3.2 2.5.6 3.6.1.3 0 .7-.2 1z"/></svg>
        0412 557 208
      </li>
      <li>
        <svg viewBox="0 0 24 24"><path d="M2 5h20v14H2z M4 7v.4l8 5 8-5V7z" fill-rule="evenodd"/></svg>
        Dale@braviotraxgroup.com
      </li>
      <li>
        <svg viewBox="0 0 24 24"><path d="M12 2a10 10 0 1 0 0 20 10 10 0 0 0 0-20zm6.9 6h-3a15 15 0 0 0-1.3-4 8 8 0 0 1 4.3 4zM12 4c.8 1.2 1.5 2.5 1.9 4h-3.8c.4-1.5 1.1-2.8 1.9-4zM4.3 14a8 8 0 0 1 0-4h3.4a16 16 0 0 0 0 4zm.8 2h3a15 15 0 0 0 1.3 4 8 8 0 0 1-4.3-4zm3-8h-3a8 8 0 0 1 4.3-4 15 15 0 0 0-1.3 4zM12 20c-.8-1.2-1.5-2.5-1.9-4h3.8c-.4 1.5-1.1 2.8-1.9 4zm2.3-6H9.7a14 14 0 0 1 0-4h4.6a14 14 0 0 1 0 4zm.3 6a15 15 0 0 0 1.3-4h3a8 8 0 0 1-4.3 4zm1.7-6a16 16 0 0 0 0-4h3.4a8 8 0 0 1 0 4z"/></svg>
        www.braviotraxgroup.com
      </li>
    </ul>
  </section>

  <section class="card card--back" aria-label="Business card back">
    <ul class="services">
      <li>Alliances</li>
      <li>Placement</li>
      <li>Training</li>
      <li>Support</li>
    </ul>
  </section>

</main>
</body>
</html>
```